rhyming dictionary website (easy)

i need a web design for my new website which for now runs on my own self made design (i am a programmer so it sucks) you can find it at http://www.lumaquill.com

i would like a nicer design that will not cause visitors to flee in disgust.

Target Market(s)

people who search for rhymes, poets, rappers, and normal birthday greeting people

Requirements
Must have
• this is what it needs to have:

1. main page which is simple and must emphasize on the search bar.

2. search result page that will emphasize on the rhyming words and make them clear and important, it also needs to be separable like in the current "design".
it also need to have a good placement of ads, not too intrusive, not too unnoticeable

3. a general page with no real content that i can fill with anything later.
Nice to have
• also the design could combine the already exist logo that you can see on the website, i added it in the uploaded files, along with its psd.

p.s:
other design i liked that you can inspire yourself from
http://www.zelvoro.com/RhymingDictionary/hello.html

```html
<!DOCTYPE html>
<html lang="en">
<head>
<meta charset="utf-8">
<title>Lumaquill – Rhyming Dictionary</title>
<link href="https://fonts.googleapis.com/css2?family=Signika:wght@400;600&family=Arimo:wght@400;700&display=swap" rel="stylesheet">
<style>
:root{
  --navy:#22225a;
  --green-top:#7fc06a;
  --green-bottom:#4f9440;
  --green-active:#3f7c32;
  --tagline:#e4f26a;
  --white:#ffffff;
  --ink:#333333;
  --muted:#8a8a8a;
  --magenta:#a11c5e;
  --pink:#d62d6d;
  --red:#b81d2c;
  --panel:#e9e9e9;
  --row:#f3f3f3;
  --line:#d6d6d6;
  --orange-top:#f08a2a;
  --orange-bottom:#c6480e;
  --link:#0645ad;
  --url:#7a7a7a;
  --footer:#d8d8ea;
}
*{margin:0;padding:0;box-sizing:border-box}
html,body{width:1200px;height:1148px;overflow:hidden}
body{position:relative;background:var(--navy);font-family:"Signika",sans-serif;color:var(--ink)}
.abs{position:absolute}

.main-nav{left:0;top:0;width:1200px;height:57px;background:linear-gradient(var(--green-top),var(--green-bottom));border-bottom:1px solid #3c6f31}
.main-nav ul{list-style:none;display:flex;position:absolute;left:90px;top:0;height:57px;border-left:1px solid #5d9a4d}
.main-nav li{height:57px;display:flex;align-items:center;padding:0 20px;color:var(--white);font-size:16px;border-right:1px solid #5d9a4d;text-shadow:0 1px 1px rgba(0,0,0,.35)}
.main-nav li.active{background:var(--green-active);padding:0 25px}

.tagline{left:0;width:1200px;top:74px;text-align:center;color:var(--tagline);font-weight:600;font-size:19px;line-height:31px}

.card{background:var(--white);border-radius:3px}
.header-card{left:90px;top:152px;width:1020px;height:173px}
.brand{left:10px;top:110px;display:flex;align-items:center;gap:10px;font-size:33px;color:#3a3a3a}
.brand-dot{width:24px;height:24px;border-radius:50%;background:#8a4fa8}
.brand-mark{left:40px;top:14px;width:100px;height:95px;border-radius:50%;background:radial-gradient(circle,#ffffff 25%,#d9d2ea 26%,#c9c0de 60%,#ffffff 61%)}
.poet-art{left:223px;top:5px;width:190px;height:163px;background:linear-gradient(135deg,#e2e2e2,#9a9a9a 60%,#cfcfcf)}
.search-label{left:415px;top:26px;color:var(--magenta);font-size:17px}
.search-box{left:416px;top:58px;width:595px;height:51px;background:var(--white);border:1px solid #dcdcdc;border-bottom:4px solid #e5e5e5}
.search-box .placeholder{position:absolute;left:19px;top:14px;color:var(--muted);font-size:15px}
.search-btn{position:absolute;right:6px;top:6px;width:75px;height:39px;border-radius:4px;background:linear-gradient(var(--orange-top),var(--orange-bottom));color:var(--white);font-weight:600;font-size:18px;display:flex;align-items:center;justify-content:center}
.latest{left:419px;top:128px;font-size:15px;color:#222}
.latest span{color:var(--muted)}

.results-card{left:90px;top:333px;width:1020px;height:658px}
.side-ad{left:11px;top:19px;width:167px;height:514px;background:linear-gradient(#eaf3fb 0%,#d8ecf8 45%,#f2c070 80%,#f08a1e 100%)}
.side-ad-shadow{left:16px;top:546px;width:152px;height:34px;border-radius:12px;background:#e6e6e6;filter:blur(3px)}
.side-ad-btn{left:20px;top:598px;width:148px;height:37px;border-radius:5px;background:linear-gradient(#a6d23a,#6ea51a);color:var(--white);font-weight:600;font-size:17px;display:flex;align-items:center;justify-content:center;gap:8px;box-shadow:0 0 0 3px #eeeeee}

.results-head{left:196px;top:19px;width:815px;height:54px;background:var(--panel)}
.results-head .label{position:absolute;left:16px;top:17px;font-size:15px;color:#666}
.results-head .keyword{color:var(--red);font-size:20px;margin-left:4px}
.results-head .note{position:absolute;right:13px;top:18px;font-size:15px;color:#888}
.result-links{left:212px;top:86px;font-size:15px;color:var(--pink)}
.result-links .sep{margin:0 13px}

.rhyme-table{left:196px;top:123px;width:815px;height:408px;border:1px solid var(--line);background:#f7f7f7}
.rhyme-row{position:absolute;left:0;width:813px;background:var(--row);border-bottom:1px solid var(--line);font-size:15px;color:#444}
.rhyme-row span{position:absolute;top:50%;transform:translateY(-50%)}
.c1{left:33px}.c2{left:235px}.c3{left:437px}.c4{left:642px}

.text-ads{left:229px;top:551px;width:780px;font-family:"Arimo",sans-serif;font-size:11px;line-height:14.5px;color:#111}
.text-ad{position:absolute;top:0;width:140px}
.text-ad a{color:var(--link);font-weight:700;text-decoration:underline}
.text-ad .url{color:var(--url);font-size:9.5px;letter-spacing:.5px}

.footer-nav{left:0;top:1022px;width:1200px;text-align:center;color:var(--footer);font-size:15px}
.footer-nav .sep{margin:0 12px}
.copyright{left:0;top:1059px;width:1200px;text-align:center;color:var(--footer);font-size:15px}
.social{left:572px;top:1097px;display:flex;gap:8px}
.social span{width:23px;height:23px;border-radius:3px;background:#5b6fb0}
.social span+span{background:#4fb2e6}
</style>
</head>
<body>

<nav class="main-nav abs">
  <ul>
    <li class="active">Home</li>
    <li>Free Rhyming Dictionary</li>
    <li>Free Letter Templates</li>
    <li>Free Business Naming</li>
    <li>Free Stationary Templates</li>
    <li>Free Taglines</li>
  </ul>
</nav>

<p class="tagline abs">So you're writing a song or a poem and are frustrated from searching for the right rhyme? Then you're in the right place!<br>Our automated system will fix you the perfect rhyme, that will make you look like the poet you always wanted to be</p>

<header class="header-card card abs">
  <div class="brand abs"><span class="brand-dot"></span>Lumaquill</div>
  <div class="poet-art abs" role="img" aria-label="Engraving of a poet writing at a desk"></div>
  <p class="search-label abs">I want to find a rhyme to the word</p>
  <div class="search-box abs">
    <span class="placeholder">Enter your Keyword...</span>
    <span class="search-btn">NOW!</span>
  </div>
  <p class="latest abs">Latest searches : &nbsp;<span>indeed, craze, cute, angel, smile</span></p>
</header>

<main class="results-card card abs">
  <div class="side-ad abs" role="img" aria-label="Vertical hosting advertisement banner with discount offer and a smiling woman holding a glass"></div>
  <div class="side-ad-shadow abs"></div>
  <div class="side-ad-btn abs">ВИЖ ОЩЕ
    <svg width="10" height="14" viewBox="0 0 10 14"><path d="M2 2l5 5-5 5" stroke="#fff" stroke-width="2.5" fill="none"/></svg>
  </div>

  <div class="results-head abs">
    <span class="label">Search results for : <span class="keyword">Your Keyword</span></span>
    <span class="note">Pellentesque hendrerit justo non nulla semper, varius malesuada.</span>
  </div>
  <p class="result-links abs">Definition of Keyword<span class="sep">::</span>Synonyms and antonyms of Keyword</p>

  <div class="rhyme-table abs">
    <div class="rhyme-row" style="top:0;height:56px"><span class="c1">Quisque sed</span><span class="c2">Donec laoreet</span><span class="c3">Praesent velit</span><span class="c4">Nunc et odio</span></div>
    <div class="rhyme-row" style="top:56px;height:59px"><span class="c1">Class aptent</span><span class="c2">Cras gravida velit</span><span class="c3">Aenean nec</span><span class="c4">Proin at duivel</span></div>
    <div class="rhyme-row" style="top:115px;height:59px"><span class="c1">Fusceelit</span><span class="c2">Nunc sed</span><span class="c3">Fusce varius feugiat</span><span class="c4">Mauris diam</span></div>
  </div>

  <div class="text-ads abs">
    <div class="text-ad" style="left:0"><a>Cheap Phuket Hotel Deals</a><br>Discount Rates on 3-5 Star Hotels Book &amp; Save Big on Phuket Hotels<br><span class="url">www.tripvane.com/hotels</span></div>
    <div class="text-ad" style="left:194px"><a>Holiday Package Phuket</a><br>Visiting Phuket? Find Deals &amp; Read Hotel Reviews!<br><span class="url">www.Travelora.com</span></div>
    <div class="text-ad" style="left:391px"><a>4 Star Bangkok Hotel</a><br>Discount rates. Close to subway, shopping, attractions, nightlife.<br><span class="url">www.orchidstay.com</span></div>
    <div class="text-ad" style="left:585px;width:150px"><a>Bangkok Hotel</a><br>460 Luxury Suites room in Bangkok Special rates online Booking Now!<br><span class="url">www.LanternSuitesHotel.com</span></div>
  </div>
</main>

<footer>
  <p class="footer-nav abs">Home<span class="sep">|</span>Free Rhyming Dictionary<span class="sep">|</span>Free Letter Templates<span class="sep">|</span>Free Business Naming<span class="sep">|</span>Free Stationary Templates<span class="sep">|</span>Free Taglines</p>
  <p class="copyright abs">Copyright &copy; 2013 &nbsp;Lumaquill. &nbsp;&nbsp;&nbsp;All rights reserved.</p>
  <div class="social abs"><span></span><span></span></div>
</footer>

</body>
</html>
```